Korvessa Foundation Website - Helping Save Lives for over 60 Years

Korvessa, a not-for-profit organization, is re-launching its website and is looking for ideas to improve our new website design, starting with our homepage. We are looking to make it clean, easy to navigate, and compelling. Our target and membership bases tend to be on the older than the medium population. Korvessa's mission is to provide information to first responders during our members' times of need, their Korvessa moments. We provide emergency health, family and physician notifications as well as assist in providing wandering support when one of our members goes missing or is found, so they can be re-united with their loved ones. Korvessa Foundation has been around since 1956.
Korvessa offers products, our Medical IDs and services, our membership plans, so people can have their alert (Medical ID) and their emergency health record that is available to first responders on a 24/7 basis via our Emergency Response Team.

Please help us make Korvessa more appealing and modern-looking so we can grow our footprint and increase our impact both in the US and worldwide.

Target Market(s)

US consumers 40+ years old

Industry/Entity Type

Non Profit

Number of Pages Required

5+ page

Font styles to use
Other font styles liked:
• looking for sans serif like font (e.g. helvetica, tahoma, etc.)

Colors

Designer to choose colors to be used in the design.

Requirements
Must have
• See word document attached
Nice to have
Should not have

```html
<!DOCTYPE html>
<html lang="en">
<head>
<meta charset="utf-8">
<title>Korvessa Foundation</title>
<link href="https://fonts.googleapis.com/css2?family=Open+Sans:wght@400;600;700;800&display=swap" rel="stylesheet">
<style>
:root{
  --teal:#0d4d69;
  --teal-dark:#093b52;
  --red:#9b2333;
  --ink:#2b2b2b;
  --muted:#777;
  --white:#fff;
  --light:#f4f6f8;
}
*{margin:0;padding:0;box-sizing:border-box}
html,body{width:1200px;height:2949px;overflow:hidden}
body{position:relative;font-family:"Open Sans",Arial,sans-serif;color:var(--ink);background:var(--white)}
.abs{position:absolute}
.btn{position:absolute;display:flex;align-items:center;justify-content:center;gap:8px;background:var(--red);color:var(--white);font-size:12px;font-weight:700;text-decoration:none}
/* top bar */
.topbar{left:0;top:0;width:1200px;height:36px;background:var(--teal)}
.social{display:flex;gap:7px}
.social span{width:12px;height:12px;border-radius:50%;background:var(--white)}
.topbar .social{position:absolute;left:151px;top:12px}
.topbar .phone{position:absolute;left:560px;top:10px;color:var(--white);font-size:10px;font-weight:700;display:flex;gap:6px;align-items:center}
.topbar .search{position:absolute;left:922px;top:11px}
.topbar .signin{position:absolute;left:948px;top:11px;color:var(--white);font-size:10px;font-weight:700}
.topbar .enroll{position:absolute;left:999px;top:0;width:52px;height:36px;background:var(--red);color:var(--white);font-size:10px;font-weight:700;display:flex;align-items:center;justify-content:center}
/* nav */
.nav{left:0;top:36px;width:1200px;height:88px;background:var(--white)}
.brand{position:absolute;display:flex;align-items:center;gap:8px;font-weight:700}
.brand .mark{border-radius:50%;border:2px solid currentColor}
.nav .brand{left:150px;top:26px;color:var(--teal-dark);font-size:22px}
.nav .brand .mark{width:34px;height:34px}
.nav ul{position:absolute;top:38px;left:590px;list-style:none;display:flex;gap:30px;font-size:11px;font-weight:700;color:#8a8a8a}
.nav li.active{color:var(--red)}
/* hero */
.hero{left:0;top:124px;width:1200px;height:482px;background:linear-gradient(180deg,#3b4a52 0%,#51616a 45%,#3a4447 100%)}
.hero h1{position:absolute;left:150px;top:98px;color:var(--white);font-size:56px;font-weight:700;line-height:64px}
.hero p{position:absolute;left:150px;top:246px;width:600px;color:var(--white);font-size:18px;font-weight:700;line-height:22px}
.hero .start{left:150px;top:326px;width:141px;height:44px}
.hero .how{left:305px;top:326px;width:139px;height:44px;background:transparent;border:3px solid var(--red)}
/* cards */
.card{top:576px;width:276px;height:274px;background:var(--teal);color:var(--white);padding:44px 46px 0;box-shadow:0 6px 16px rgba(0,0,0,.12)}
.card h2{font-size:27px;font-weight:700;margin-bottom:18px}
.card p{font-size:11.5px;font-weight:700;line-height:19px}
/* feature */
.feature-img{left:443px;top:940px;width:554px;height:268px;background:linear-gradient(120deg,#7a3238,#a24a4c 55%,#8a3a40)}
.feature-card{left:203px;top:960px;width:436px;height:228px;background:var(--light);padding:36px 36px;box-shadow:0 6px 18px rgba(0,0,0,.15)}
.feature-card h3{font-size:18px;font-weight:700;line-height:27px;margin-bottom:14px}
.feature-card p{font-size:11.5px;font-weight:600;color:var(--muted);line-height:17px}
.feature-card .btn{left:36px;top:170px;width:96px;height:30px}
/* empower */
.empower{left:0;top:1300px;width:1200px;height:374px;background:linear-gradient(180deg,#1e5a73,#245f77 50%,#1b5168)}
.empower h2{position:absolute;left:0;width:1200px;top:84px;text-align:center;color:var(--white);font-size:27px;font-weight:700}
.empower p{position:absolute;left:380px;width:440px;top:166px;text-align:center;color:var(--white);font-size:13px;font-weight:700;line-height:20px}
.empower .btn{left:521px;top:256px;width:158px;height:28px}
/* testimonial */
.quote{left:222px;top:1766px;width:350px;height:207px;background:var(--white);border-top:4px solid var(--red);box-shadow:0 4px 16px rgba(0,0,0,.18);padding:22px 44px 0}
.quote .qm{text-align:center;color:#aaa;font-size:18px;font-weight:700;line-height:18px}
.quote p{font-size:11px;font-weight:700;line-height:17px;margin-top:6px}
.quote .who{font-size:11px;font-weight:700;margin-top:4px;padding-left:18px}
.quote .who b{color:var(--red)}
.quote .who span{color:var(--teal)}
.dots{position:absolute;left:160px;bottom:18px;display:flex;gap:5px}
.dots i{width:7px;height:7px;border-radius:50%;background:#bbb}
.dots i:first-child{background:var(--teal)}
.speaks{left:616px;top:1806px;font-size:27px;font-weight:700;line-height:36px}
.speaks-btn{left:620px;top:1894px;width:95px;height:30px}
/* partners */
.partners h2{position:absolute;left:0;top:2052px;width:1200px;text-align:center;font-size:27px;font-weight:700;line-height:36px}
.badge{top:2158px;height:30px;border-radius:3px;background:#cfd6dc}
.partners .btn{left:518px;top:2219px;width:164px;height:28px}
/* cta */
.cta{left:238px;top:2337px;width:724px;height:197px;background:var(--teal);color:var(--white);text-align:center}
.cta h2{margin-top:22px;font-size:27px;font-weight:700}
.cta p{width:460px;margin:16px auto 0;font-size:11.5px;font-weight:700;line-height:17px}
.cta .btn{left:295px;top:142px;width:98px;height:28px}
/* footer */
.footer{left:0;top:2626px;width:1200px;height:285px;background:linear-gradient(90deg,#2c6981,#1f5b73 40%,#276880)}
.footer .brand{left:150px;top:40px;color:var(--white);font-size:24px}
.footer .brand .mark{width:36px;height:36px}
.fhead{position:absolute;color:var(--white);font-size:12px;font-weight:700}
.fhead::after{content:"";display:block;width:60px;height:3px;background:var(--red);margin-top:5px}
.footer .links{position:absolute;left:568px;top:74px;list-style:none;color:var(--white);font-size:10px;font-weight:700;line-height:21px}
.sub-note{position:absolute;left:150px;top:185px;color:var(--white);font-size:10px;font-weight:700}
.email{position:absolute;left:150px;top:210px;width:188px;height:32px;background:var(--white);color:#aaa;font-size:11px;padding:9px 12px}
.subscribe{left:338px;top:210px;width:86px;height:32px;font-size:10px}
.pay{position:absolute;top:220px;display:flex;gap:8px;left:533px}
.pay span{width:38px;height:26px;border-radius:3px;background:#dfe6ea}
.contact-row{position:absolute;left:844px;display:flex;gap:14px;align-items:flex-start;color:var(--white);font-size:10px;font-weight:700;line-height:14px}
.footer .social{position:absolute;left:844px;top:228px}
.footer .social span{width:16px;height:16px}
.copy{left:0;top:2911px;width:1200px;height:38px;background:var(--teal-dark);color:var(--white);font-size:9px;font-weight:700;display:flex;align-items:center;justify-content:center}
</style>
</head>
<body>

<header class="abs topbar">
  <div class="social"><span></span><span></span><span></span><span></span></div>
  <div class="phone">
    <svg width="10" height="10" viewBox="0 0 24 24"><path fill="#fff" d="M6.6 10.8a15 15 0 0 0 6.6 6.6l2.2-2.2c.3-.3.7-.4 1-.2 1.1.4 2.3.6 3.6.6.6 0 1 .4 1 1V20c0 .6-.4 1-1 1A17 17 0 0 1 3 4c0-.6.4-1 1-1h3.5c.6 0 1 .4 1 1 0 1.3.2 2.5.6 3.6.1.3 0 .7-.2 1z"/></svg>
    +855.410.2281
  </div>
  <svg class="search" width="12" height="12" viewBox="0 0 24 24"><circle cx="10" cy="10" r="7" fill="none" stroke="#fff" stroke-width="2.5"/><path d="M15 15l6 6" stroke="#fff" stroke-width="2.5"/></svg>
  <span class="signin">SIGN IN</span>
  <span class="enroll">ENROLL</span>
</header>

<nav class="abs nav">
  <div class="brand"><span class="mark"></span>Korvessa</div>
  <ul>
    <li class="active">HOME</li><li>ABOUT</li><li>MEMBERSHIP</li><li>MEDICAL ID</li><li>DONATE</li><li>CONTACT</li>
  </ul>
</nav>

<section class="abs hero" role="img" aria-label="Photo of a grandfather and child walking along the seashore">
  <h1>Protect yourself<br>and your loved ones</h1>
  <p>With Korvessa, first responders and health professionals have access to your vital information in any time of need.</p>
  <a class="btn start">Get started</a>
  <a class="btn how">How it works
    <svg width="14" height="14" viewBox="0 0 24 24"><circle cx="12" cy="12" r="11" fill="#fff"/><path d="M10 7l6 5-6 5z" fill="var(--teal)"/></svg>
  </a>
</section>

<article class="abs card" style="left:150px">
  <h2>Who</h2>
  <p>We provide Medical IDs, paired with 24/7 life saving services to millions of people in the United States and around the world since 1956.</p>
</article>
<article class="abs card" style="left:462px">
  <h2>What</h2>
  <p>In emergencies, we provide member’s information to first responders. This information exchange empowers them to make informed decisions about care and safety of our members.</p>
</article>
<article class="abs card" style="left:775px">
  <h2>Why</h2>
  <p>We ultimately exist to save and protect lives. We want to provide peace of mind for anyone, anywhere at any time.</p>
</article>

<div class="abs feature-img" role="img" aria-label="Photo of a mother and child touching noses"></div>
<div class="abs feature-card">
  <h3>No one should have to face an<br>emergency alone</h3>
  <p>More than just a piece of jewelry, We provides our members life-saving information services, supported with an internationally recognized Medical ID.</p>
  <a class="btn">Know more</a>
</div>

<section class="abs empower" role="img" aria-label="Photo of first responders at work, tinted teal">
  <h2>Empower first responders</h2>
  <p>In emergencies, we provide member’s information to first responders. This information exchange empowers them to make informed decisions about care and safety of our members.</p>
  <a class="btn">More on membership</a>
</section>

<blockquote class="abs quote">
  <div class="qm">“</div>
  <p>I could be anywhere and eat something that Triggers a reaction. So if I can’t speak for myself it is good to know that the information on my Bracelet will let someone know what my condition is and and provide the help I need.</p>
  <div class="who"><b>- Dale Perrin</b> <span>Member since 2006</span></div>
  <div class="dots"><i></i><i></i><i></i></div>
</blockquote>
<h2 class="abs speaks">Korvessa speaks for its<br>members in an emergency</h2>
<a class="btn speaks-btn">Donate</a>

<section class="partners">
  <h2>Because of our partners, we are doing<br>more good for more people.</h2>
  <div class="abs badge" style="left:444px;width:72px"></div>
  <div class="abs badge" style="left:552px;width:66px"></div>
  <div class="abs badge" style="left:668px;width:68px"></div>
  <a class="btn">Meet our partners</a>
</section>

<section class="abs cta">
  <h2>Get started with Korvessa today!</h2>
  <p>With Korvessa, first responders and health professional have access to your Vital information in any time of need.</p>
  <a class="btn">Enroll now</a>
</section>

<footer class="abs footer" role="img" aria-label="Teal-tinted photo of a paramedic helping a patient">
  <div class="brand"><span class="mark"></span>Korvessa</div>
  <div class="fhead" style="left:150px;top:152px">STAY UPDATED</div>
  <div class="sub-note">SUBSCRIBE TO OUR MAILING LIST TO GET OUR LATEST UPDATES.</div>
  <div class="email">email</div>
  <a class="btn subscribe">SUBSCRIBE</a>

  <div class="fhead" style="left:568px;top:43px">HOME</div>
  <ul class="links"><li>ABOUT</li><li>MEMBERSHIP</li><li>MEDICAL ID</li><li>DONATION</li><li>CONTACT</li></ul>
  <div class="pay"><span></span><span></span><span></span></div>

  <div class="fhead" style="left:844px;top:43px">CONTACT</div>
  <div class="contact-row" style="top:84px">
    <svg width="16" height="20" viewBox="0 0 24 30"><path fill="#fff" d="M12 0C5.4 0 0 5.2 0 11.6 0 20.3 12 30 12 30s12-9.7 12-18.4C24 5.2 18.6 0 12 0zm0 16a4.5 4.5 0 1 1 0-9 4.5 4.5 0 0 1 0 9z"/></svg>
    <span>HARLOW HOUSE<br>SUITE 12, 48 VANTOR LANE<br>BRENFIELD, OSTRIA 4127</span>
  </div>
  <div class="contact-row" style="top:140px">
    <svg width="18" height="13" viewBox="0 0 24 17"><rect width="24" height="17" rx="2" fill="#fff"/><path d="M1 1l11 8 11-8" fill="none" stroke="var(--teal)" stroke-width="1.8"/></svg>
    <span>hello@korvessa-mail.org</span>
  </div>
  <div class="contact-row" style="top:183px">
    <svg width="17" height="17" viewBox="0 0 24 24"><path fill="#fff" d="M6.6 10.8a15 15 0 0 0 6.6 6.6l2.2-2.2c.3-.3.7-.4 1-.2 1.1.4 2.3.6 3.6.6.6 0 1 .4 1 1V20c0 .6-.4 1-1 1A17 17 0 0 1 3 4c0-.6.4-1 1-1h3.5c.6 0 1 .4 1 1 0 1.3.2 2.5.6 3.6.1.3 0 .7-.2 1z"/></svg>
    <span>+1300 482 917</span>
  </div>
  <div class="social"><span></span><span></span><span></span><span></span></div>
</footer>
<div class="abs copy">© COPYRIGHT 2018. ALL RIGHTS RESERVED.</div>

</body>
</html>
```